Stunning Podcast Cover Design for The Morning Brook Hour!!

I need a design for my new podcast.
I will need it in a variety of size/formats, such as a large version for my podcast website homepage, the thumbnail for TuneVault, Loomcast, Pindle Store and more.

The podcast is called "The Morning Brook Hour" and it includes topics such as: business, entrepreneurship, finance, budgeting, estate planning, end-of-life planning, travel, business and personal stories featuring people from all over the world, life in general, and more.

I don't have a vision in mind so am looking for creativity but it definitely needs to have the colour gold in it somewhere! No cartoon characters please.

I will provide comments/feedback to each designer.

***UPDATE: Please see some photos of me that can be used in the podcast design.

Here is some tips on creating podcast designs. https://www.wavernest.com/blog/10-tips-create-awesome-podcast-artwork

Target Market(s)

Adults 25 - 65

Font styles to use
Other font styles liked:
• something modern - see my company logo as an example

Colors

Designer to choose colors to be used in the design.

Requirements
Must have
• The colour gold in it
Nice to have
• I feel like the word "The" should be smaller then the other three words.
• I would like to see designs with a white coloured background and a black coloured one also...
• Perhaps designs with a filter over the photo, and without.
• Perhaps use my photo, or don't use my photo!
• Please see some photos of me that can be used in the podcast design.
• Here is some tips on creating podcast designs. https://www.wavernest.com/blog/10-tips-create-awesome-podcast-artwork
Should not have
• cartoon characters
• Corny 1990's "Evenings with the Grand and Glittering" look - see https://www.clipharbor.com/watch?v=Q7T2KX8PLWZ

```html
<!DOCTYPE html>
<html lang="en">
<head>
<meta charset="utf-8">
<title>The Morning Brook Hour — Podcast Cover</title>
<link href="https://fonts.googleapis.com/css2?family=Montserrat:wght@900&display=swap" rel="stylesheet">
<style>
  :root {
    --page: #ffffff;
    --cover-black: #000000;
    --frame-gold: #f2c200;
    --title-white: #ffffff;
    --gold-top: #ffd400;
    --gold-bottom: #ff8c00;
    --glow-top: #6e5600;
    --glow-bottom: #5f3c00;
    --host-light: #b9a9a0;
    --host-dark: #6a5148;
  }
  html, body {
    margin: 0;
    padding: 0;
    width: 1198px;
    height: 1200px;
    overflow: hidden;
    background: var(--page);
  }
  .cover {
    display: block;
    width: 1198px;
    height: 1200px;
  }
  .cover-title {
    font-family: "Montserrat", sans-serif;
    font-weight: 900;
  }
  .title-small { fill: var(--title-white); }
  .title-large {
    fill: url(#goldFill);
    stroke: var(--title-white);
    stroke-width: 3px;
    paint-order: stroke;
  }
</style>
</head>
<body>
<svg class="cover" viewBox="0 0 1198 1200" xmlns="http://www.w3.org/2000/svg">
  <defs>
    <linearGradient id="goldFill" x1="0" y1="0" x2="0" y2="1">
      <stop offset="0" stop-color="var(--gold-top)"/>
      <stop offset="1" stop-color="var(--gold-bottom)"/>
    </linearGradient>
    <radialGradient id="glowFill" cx="0.5" cy="0.5" r="0.5">
      <stop offset="0" stop-color="var(--glow-top)" stop-opacity="0.85"/>
      <stop offset="0.6" stop-color="var(--glow-bottom)" stop-opacity="0.55"/>
      <stop offset="1" stop-color="var(--glow-bottom)" stop-opacity="0"/>
    </radialGradient>
    <linearGradient id="hostFill" x1="0" y1="0" x2="0" y2="1">
      <stop offset="0" stop-color="var(--host-dark)"/>
      <stop offset="0.45" stop-color="var(--host-light)"/>
      <stop offset="1" stop-color="var(--host-dark)"/>
    </linearGradient>
    <clipPath id="coverClip">
      <rect x="42" y="42" width="1118" height="1115" rx="22"/>
    </clipPath>
  </defs>

  <rect class="cover-base" x="42" y="42" width="1118" height="1115" rx="22" fill="var(--cover-black)"/>

  <g clip-path="url(#coverClip)">
    <ellipse class="background-emblem" role="img" aria-label="Large faint gold currency emblem behind the title"
             cx="360" cy="620" rx="320" ry="560" fill="url(#glowFill)"/>
  </g>

  <rect class="cover-frame" x="58" y="58" width="1086" height="1084" rx="16" fill="none" stroke="var(--frame-gold)" stroke-width="2"/>

  <g clip-path="url(#coverClip)">
    <path class="host-photo" role="img" aria-label="Portrait photo of the smiling host with long brown hair and glasses"
          d="M592 1160 L620 900 Q650 640 830 575 Q960 540 1060 610 Q1130 700 1120 950 L1116 1160 Z"
          fill="url(#hostFill)"/>
  </g>

  <g class="cover-title">
    <text class="title-small" x="100" y="212" font-size="154" textLength="298" lengthAdjust="spacingAndGlyphs">THE</text>
    <text class="title-large" x="116" y="422" font-size="277" textLength="912" lengthAdjust="spacingAndGlyphs">MORNING</text>
    <text class="title-large" x="116" y="652" font-size="277" textLength="636" lengthAdjust="spacingAndGlyphs">BROOK</text>
    <text class="title-small" x="104" y="796" font-size="177" textLength="540" lengthAdjust="spacingAndGlyphs">HOUR</text>
  </g>
</svg>
</body>
</html>
```